Graphic Design for Free Community Event

We need a graphic created for a community event that is aimed at families with younger children called Totz Jam. This is a free event and has a fair/carnival feel to it with rides, games, and food. I need the graphic to be flexible enough to be able to be modified and used in a variety of ways on different print and digital marketing materials. I also need the centerpiece of the design to be an event logo that can be used as a standalone element.

The overall feel needs to be fun and friendly with a slightly modern edge to it. Attached are some images used in past events. These are for reference only and do not need to be simulated or used in the final product.

Target Market(s)

Families with children

Industry/Entity Type

Church

Font styles to use
Sans Serif

Requirements
Must have
• - Logo that incorporates the event name- Event Date: August 20 - Event Time: 10am - 2pm - Church name and logo incorporated: Bright Harbor Community Church (see attached logo files)
Nice to have
• - Bright colors- Flexible design elements that are interchangeable and scalable for use of the design in different layouts across different mediums and materials.
Should not have
• - Any references or images related to drugs, alcohol, tobacco, or other subjects that would be inappropriate for children.

```html
<!DOCTYPE html>
<html lang="en">
<head>
<meta charset="utf-8">
<title>Totz Jam – Bright Harbor Community Church</title>
<link rel="stylesheet" href="https://fonts.googleapis.com/css2?family=Rammetto+One&family=Michroma&family=Syncopate:wght@700&family=Open+Sans:wght@800&display=swap">
<style>
  :root {
    --sky: #8af0f4;
    --royal: #0447c7;
    --navy: #0b3aa8;
    --orange: #e5791c;
    --sun: #f6d930;
    --lemon: #f9f35a;
    --pink: #e0586f;
    --cobalt: #3552e6;
    --ink: #222226;
  }
  * { margin: 0; padding: 0; box-sizing: border-box; }
  html, body { width: 1200px; height: 675px; overflow: hidden; background: var(--sky); }
  .poster { position: relative; width: 1200px; height: 675px; background: var(--sky); overflow: hidden; }

  .event-title { position: absolute; left: 0; top: 0; width: 640px; height: 200px; }
  .event-title text { font-family: "Rammetto One", sans-serif; fill: var(--royal); }

  .confetti { position: absolute; left: 0; top: 200px; width: 360px; height: 280px; }
  .corner-dots { position: absolute; right: 90px; top: -15px; width: 44px; height: 210px; }
  .stripe-band { position: absolute; right: 0; top: 255px; width: 160px; height: 320px; }

  .event-photo {
    position: absolute; left: 463px; top: 109px; width: 669px; height: 446px;
    background: linear-gradient(160deg, #c9a57a 0%, #8fb0c8 30%, #d9c4b8 55%, #3f4f7a 75%, #efe6d6 100%);
    box-shadow: 0 4px 14px rgba(0,0,0,0.18);
  }

  .free-badge { position: absolute; left: 375px; top: 233px; width: 130px; height: 130px; }
  .free-badge-text {
    position: absolute; left: 403px; top: 268px; width: 80px;
    font-family: "Open Sans", sans-serif; font-weight: 800;
    color: var(--royal); transform: rotate(-12deg); line-height: 1.05;
  }
  .free-badge-text .line-one { display: block; font-size: 25px; }
  .free-badge-text .line-two { display: block; font-size: 22px; }

  .event-when {
    position: absolute; left: 47px; top: 549px;
    font-family: "Michroma", sans-serif; font-size: 15px; color: var(--navy);
    font-weight: 700; white-space: nowrap; word-spacing: 4px;
  }
  .event-when .time { margin-left: 20px; }

  .host-name { position: absolute; left: 45px; top: 575px; width: 910px; height: 40px; }
  .host-name text { font-family: "Syncopate", sans-serif; font-weight: 700; fill: var(--navy); }

  .activities {
    position: absolute; left: 0; top: 627px; width: 960px; height: 20px;
    font-family: "Michroma", sans-serif; font-size: 15px; color: var(--orange);
    list-style: none; white-space: nowrap;
  }
  .activities li { position: absolute; top: 0; }

  .church-mark { position: absolute; left: 1008px; top: 591px; display: flex; align-items: center; gap: 5px; }
  .church-mark .mark-dot { width: 50px; height: 50px; border-radius: 50%; background: var(--ink); flex: none; }
  .church-mark .mark-name {
    font-family: "Michroma", sans-serif; font-size: 8px; line-height: 1.4; color: var(--ink);
    white-space: nowrap;
  }
</style>
</head>
<body>
<main class="poster">

  <svg class="event-title" viewBox="0 0 640 200" role="img" aria-label="Totz Jam">
    <text x="22" y="166" font-size="86" textLength="560" lengthAdjust="spacingAndGlyphs" transform="rotate(-10 22 166)">TOTZ JAM</text>
  </svg>

  <svg class="confetti" viewBox="0 200 360 280" aria-hidden="true">
    <circle cx="138" cy="241" r="10" fill="var(--pink)"/>
    <circle cx="208" cy="256" r="22" fill="none" stroke="var(--pink)" stroke-width="7"/>
    <circle cx="268" cy="253" r="6.5" fill="var(--cobalt)"/>
    <polyline points="313,226 320,236 312,246 320,256 312,266 320,276 313,282" fill="none" stroke="var(--lemon)" stroke-width="2.5"/>
    <rect x="110" y="281" width="36" height="36" fill="var(--cobalt)" transform="rotate(18 128 299)"/>
    <polygon points="135,355 193,290 280,393" fill="var(--lemon)"/>
    <g fill="var(--cobalt)">
      <circle cx="212" cy="324" r="2"/><circle cx="199" cy="341" r="2"/><circle cx="214" cy="341" r="2"/>
      <circle cx="233" cy="341" r="2"/><circle cx="196" cy="358" r="2"/><circle cx="215" cy="358" r="2"/>
      <circle cx="230" cy="356" r="2"/><circle cx="248" cy="353" r="2"/><circle cx="227" cy="370" r="2"/>
    </g>
    <polygon points="289,345 324,398 266,433" fill="var(--orange)"/>
    <circle cx="296" cy="325" r="4" fill="var(--cobalt)"/>
    <circle cx="232" cy="422" r="7" fill="var(--cobalt)"/>
    <circle cx="169" cy="458" r="10" fill="var(--orange)"/>
    <polyline points="94,451 112,451 118,438 124,447 132,432 140,427" fill="none" stroke="var(--lemon)" stroke-width="2.5"/>
  </svg>

  <svg class="stripe-band" viewBox="0 0 160 320" aria-hidden="true">
    <g fill="var(--orange)">
      <polygon points="90,40 120,55 40,310 10,305"/>
      <polygon points="145,70 160,80 160,130 80,312 55,312"/>
      <polygon points="160,190 160,240 125,305 100,312"/>
    </g>
  </svg>

  <div class="event-photo" role="img" aria-label="Photo of smiling friends sharing cotton candy in front of a lit fairground carousel"></div>

  <svg class="corner-dots" viewBox="0 -15 44 210" aria-hidden="true">
    <circle cx="22" cy="5" r="20" fill="var(--sun)"/>
    <circle cx="22" cy="58" r="20" fill="var(--orange)"/>
    <circle cx="22" cy="114" r="20" fill="var(--sun)"/>
    <circle cx="22" cy="169" r="20" fill="var(--orange)"/>
  </svg>

  <svg class="free-badge" viewBox="0 0 130 130" aria-hidden="true">
    <polygon fill="var(--sun)" points="65,0 73,12 86,4 89,18 104,15 101,29 116,31 108,43 122,50 110,59 120,70 106,75 113,88 98,90 100,105 86,102 84,117 71,110 65,124 57,111 45,119 42,104 28,108 29,93 14,92 21,79 7,72 18,62 6,52 20,46 13,33 28,31 25,16 40,19 43,5 56,12" transform="rotate(6 65 65) translate(0 3)"/>
  </svg>
  <p class="free-badge-text"><span class="line-one">FREE</span><span class="line-two">ENTRY</span></p>

  <p class="event-when"><span class="date">AUGUST 20</span><span class="time">10AM - 2PM</span></p>

  <svg class="host-name" viewBox="0 0 910 40" aria-label="Bright Harbor Community Church">
    <text x="0" y="33" font-size="34" textLength="905" lengthAdjust="spacingAndGlyphs">BRIGHT HARBOR COMMUNITY CHURCH</text>
  </svg>

  <ul class="activities">
    <li style="left:48px">BUNGEE JUMP</li>
    <li style="left:295px">FOOD</li>
    <li style="left:433px">ROCK WALL</li>
    <li style="left:652px">RIDES</li>
    <li style="left:793px">INFLATABLES</li>
  </ul>

  <div class="church-mark">
    <span class="mark-dot"></span>
    <p class="mark-name">BRIGHT HARBOR<br>COMMUNITY CHURCH</p>
  </div>

</main>
</body>
</html>
```